Two wall artworks for physiotherapy clinic waiting room

We are a physiotherapy clinic located in Glebe, Sydney. We have a clinic that is within a beautiful heritage listed building and we have two blank white walls that need artwork. Each artwork will be 3000mm wide and 1200mm high. Our clinic is mostly white and I will include our brand's colours below. We are looking for bright, beautiful artworks that are consistent with our colours. One of the artworks should include our full logo including the text so that customers see the name of the clinic on their way into the waiting room. I will include our logo in the files below, as well as images of the clinic, the walls and some other signs that we have already. We would prefer artworks with nice patterns or graphics rather than images of people.

```html
<!DOCTYPE html>
<html lang="en">
<head>
<meta charset="utf-8">
<title>Elmwood Physio – Waiting Room Wall Artworks</title>
<link href="https://fonts.googleapis.com/css2?family=Montserrat:wght@500;600&display=swap" rel="stylesheet">
<style>
  :root {
    --page: #ffffff;
    --wall: #ebebea;
    --wall-shade: #dcdcda;
    --navy: #1e1a5c;
    --navy-deep: #231b66;
    --teal: #3cc6b6;
    --teal-light: #52d6c6;
    --sky: #8fb9e0;
    --stone: #d9d4c8;
    --white: #ffffff;
  }
  * { margin: 0; padding: 0; box-sizing: border-box; }
  html, body {
    width: 1200px; height: 746px; overflow: hidden;
    background: var(--page);
    font-family: "Montserrat", Arial, sans-serif;
  }
  .canvas { position: relative; width: 1200px; height: 746px; }

  .artwork { position: absolute; left: 49px; width: 1096px; height: 284px; overflow: hidden; }

  /* Artwork one: name wall */
  .artwork--name { top: 58px; background: radial-gradient(ellipse at 50% 45%, var(--wall) 40%, var(--wall-shade) 100%); }
  .artwork--name .flow { position: absolute; inset: 0; width: 100%; height: 100%; }
  .artwork--name .brand {
    position: absolute; left: 0; right: 0; top: 92px;
    display: flex; align-items: center; justify-content: center; gap: 26px;
    color: var(--navy);
  }
  .brand-dot { width: 54px; height: 54px; border-radius: 50%; background: var(--teal); flex: none; }
  .brand-text { display: flex; flex-direction: column; align-items: flex-end; }
  .brand-name { font-size: 62px; font-weight: 600; line-height: 1; letter-spacing: 0.5px; }
  .brand-tagline { font-size: 20px; font-weight: 500; margin-top: 12px; }

  /* Artwork two: building wall */
  .artwork--building { top: 377px; background: var(--teal); }
  .building-photo {
    position: absolute; left: 0; top: 0; width: 720px; height: 100%;
    background:
      linear-gradient(90deg, rgba(60,198,182,0) 55%, var(--teal) 100%),
      linear-gradient(180deg, var(--sky) 0%, var(--stone) 35%, #c9c2b3 70%, #7a8f6a 100%);
  }
  .artwork--building .brand {
    position: absolute; right: 32px; bottom: 34px;
    display: flex; align-items: center; gap: 20px; color: var(--white);
  }
  .artwork--building .brand-dot { width: 44px; height: 44px; background: var(--white); }
  .artwork--building .brand-name { font-size: 40px; font-weight: 500; }
  .artwork--building .brand-tagline { font-size: 14px; font-weight: 600; margin-top: 8px; }
</style>
</head>
<body>
<main class="canvas">

  <section class="artwork artwork--name">
    <svg class="flow" viewBox="0 0 1096 284" preserveAspectRatio="none" role="img" aria-label="Flowing teal and navy abstract shapes with fine line waves in the corners">
      <path d="M0 0 H60 C120 40 60 110 140 150 C210 185 230 230 190 284 H0 Z" fill="var(--teal)"/>
      <path d="M0 150 C60 170 130 160 150 210 C165 245 160 270 170 284 H0 Z" fill="var(--navy-deep)"/>
      <path d="M1096 0 H1040 C1000 30 1010 80 1060 100 C1080 108 1096 112 1096 112 Z" fill="var(--teal)"/>
      <path d="M1096 40 C1020 50 960 100 950 160 C940 210 880 200 790 240 C760 255 750 270 755 284 H1096 Z" fill="var(--teal)"/>
      <path d="M1096 45 C1030 60 990 110 985 170 C980 220 960 250 930 284 H1096 Z" fill="var(--navy-deep)"/>
    </svg>
    <div class="brand">
      <span class="brand-dot" aria-hidden="true"></span>
      <div class="brand-text">
        <span class="brand-name">Elmwood Physio</span>
        <span class="brand-tagline">Physiotherapy and Exercise Physiology</span>
      </div>
    </div>
  </section>

  <section class="artwork artwork--building">
    <div class="building-photo" role="img" aria-label="Photograph of the clinic's heritage sandstone building with a leafy tree, fading into teal"></div>
    <div class="brand">
      <span class="brand-dot" aria-hidden="true"></span>
      <div class="brand-text">
        <span class="brand-name">Elmwood Physio</span>
        <span class="brand-tagline">Physiotherapy and Exercise Physiology</span>
      </div>
    </div>
  </section>

</main>
</body>
</html>
```